Product Design for VelMira

Design Brief for VelMira Product Packaging

Objective:
Create a cohesive, elegant, and brand-consistent packaging design for the VelMira product line. The signature visual theme should reflect luxury, femininity, and clean beauty values.

---

🎨 Core Design Direction

Unified Aesthetic: All containers must prominently feature the floral pattern shown in "Pattern Reference: Image 3". This design serves as the brand's signature aesthetic and must be applied uniformly across all SKUs.

Brand Logo Placement: The VelMira logo (provided) should be clearly visible and harmoniously integrated into the patterned background.

Color Palette: Base colors should complement the brand’s primary palette: black, blush pink, and white.

---

🧴 Product-Specific Packaging Specifications

1. Mascara

Bottle Type: Sleek mascara tube with a wand applicator

Capacity: 5ml

Design: Use floral pattern from Pattern Reference Image 3. Ensure the pattern does not obstruct the readability of the logo or any regulatory text.

2. Eyebrow Growth Serum

Bottle Type: 5ml tube with fine-tip brush applicator

Capacity: 5ml

Design: Same floral pattern, scaled and applied proportionally to match the mascara for consistency

3. Eyelash Growth Serum

Bottle Type: 5ml tube with fine-tip brush (similar to the eyebrow serum, unless otherwise advised)

Capacity: 5ml

Design: Identical styling to maintain unity across lash & brow products

4. Anti-Aging Serum or Lotion

Bottle Type: 30ml airless pump bottle (preferred for hygiene and product stability)

Capacity: 30ml

Design: Apply floral pattern from Pattern Reference and scale appropriately for larger surface area

5. Hair Growth Spray

Bottle Type: 50ml fine mist spray bottle

Capacity: 50ml

Design: Pattern applied and scaled for taller profile; maintain visual harmony with skincare line

---

📦 Additional Notes

Please ensure packaging aligns with clean beauty standards (no overly glossy plastic finishes, avoid excessive secondary packaging unless sustainable).

Materials should be eco-conscious where possible.

If embossing, foil stamping, or UV finishing is available for logo accents, please suggest options.

```html
<!DOCTYPE html>
<html lang="en">
<head>
<meta charset="utf-8">
<title>VelMira Anti-Aging Serum Label</title>
<link rel="stylesheet" href="https://fonts.googleapis.com/css2?family=Playfair+Display:wght@400;800&display=swap">
<style>
  :root {
    --blush-base: #fbe3d9;
    --blush-light: #fdf0ea;
    --blush-deep: #f6cfc1;
    --petal-pink: #efb2b8;
    --petal-peach: #eeb9a2;
    --petal-core: #e79b82;
    --teal-ink: #2e6e70;
  }
  * { margin: 0; padding: 0; box-sizing: border-box; }
  html, body {
    width: 1200px;
    height: 1164px;
    overflow: hidden;
    background: var(--blush-base);
  }
  .label {
    position: relative;
    width: 1200px;
    height: 1164px;
    overflow: hidden;
    background:
      radial-gradient(ellipse at 30% 20%, var(--blush-light) 0%, transparent 55%),
      radial-gradient(ellipse at 70% 80%, var(--blush-deep) 0%, transparent 60%),
      linear-gradient(160deg, var(--blush-light) 0%, var(--blush-base) 50%, var(--blush-deep) 100%);
  }
  .floral {
    position: absolute;
    border-radius: 50%;
  }
  .floral--pink {
    background: radial-gradient(circle, var(--petal-core) 0%, var(--petal-pink) 22%, rgba(239,178,184,0.55) 60%, rgba(239,178,184,0) 75%);
  }
  .floral--peach {
    background: radial-gradient(circle, var(--petal-core) 0%, var(--petal-peach) 22%, rgba(238,185,162,0.5) 60%, rgba(238,185,162,0) 75%);
  }
  .floral--top-left     { left: -37px; top: 19px;  width: 276px; height: 276px; }
  .floral--top-center   { left: 428px; top: -111px; width: 296px; height: 296px; }
  .floral--top-right    { left: 894px; top: -28px; width: 314px; height: 314px; }
  .floral--branch-left  { left: 0;     top: 424px; width: 309px; height: 405px; border-radius: 45%; }
  .floral--tulip-right  { left: 977px; top: 447px; width: 223px; height: 300px; border-radius: 45%; }
  .floral--bottom-left  { left: 138px; top: 793px; width: 258px; height: 371px; border-radius: 45%; }
  .floral--bottom-right { left: 774px; top: 737px; width: 318px; height: 427px; border-radius: 45%; }

  .brand-name {
    position: absolute;
    left: 0;
    width: 100%;
    top: 232px;
    text-align: center;
    font-family: "Playfair Display", Georgia, serif;
    font-weight: 400;
    font-size: 140px;
    line-height: 1;
    color: var(--teal-ink);
    letter-spacing: 1px;
  }
  .product-name {
    position: absolute;
    left: 0;
    width: 100%;
    top: 540px;
    text-align: center;
    font-family: "Playfair Display", Georgia, serif;
    font-weight: 800;
    font-size: 86px;
    line-height: 112px;
    color: var(--teal-ink);
  }
  .product-volume {
    position: absolute;
    left: 0;
    width: 100%;
    top: 936px;
    text-align: center;
    font-family: "Playfair Display", Georgia, serif;
    font-weight: 800;
    font-size: 86px;
    line-height: 1.2;
    color: var(--teal-ink);
  }
</style>
</head>
<body>
  <main class="label">
    <div class="floral floral--pink floral--top-left" role="img" aria-label="Watercolor pink five-petal flower"></div>
    <div class="floral floral--pink floral--top-center" role="img" aria-label="Watercolor pink flower at the top edge"></div>
    <div class="floral floral--pink floral--top-right" role="img" aria-label="Watercolor pale pink flower with veined petals"></div>
    <div class="floral floral--peach floral--branch-left" role="img" aria-label="Watercolor peach blossom branch with leaves"></div>
    <div class="floral floral--pink floral--tulip-right" role="img" aria-label="Watercolor pink tulip bud on a stem"></div>
    <div class="floral floral--peach floral--bottom-left" role="img" aria-label="Watercolor peach flower with stem and leaves"></div>
    <div class="floral floral--peach floral--bottom-right" role="img" aria-label="Watercolor peach flower with stem and leaves"></div>

    <h1 class="brand-name">VelMira</h1>
    <h2 class="product-name">Anti-Aging<br>Serum</h2>
    <p class="product-volume">30ml</p>
  </main>
</body>
</html>
```